Business Card Design Project

Business Card
We are rebranding with a new logo
Industry/Entity Type
Business
Contact Information for Business Card
Dennis Marlow +61 427581962 dennis@qovo.com.au P.O. Box 872 Kelvindale QLD 4309
Requirements
Must have
- Logo

```html
<!DOCTYPE html>
<html lang="en">
<head>
<meta charset="utf-8">
<title>Qovo International – Business Card</title>
<link rel="stylesheet" href="https://fonts.googleapis.com/css2?family=Open+Sans:wght@400;600;700&display=swap">
<style>
  :root {
    --stage: #0b0b0b;
    --card: #ffffff;
    --blue: #2f9fd8;
    --blue-deep: #2a6f9e;
    --orange: #f0802f;
    --orange-light: #f9a23c;
    --ink: #3a3a3a;
  }
  * { box-sizing: border-box; margin: 0; padding: 0; }
  html, body {
    width: 1200px; height: 1000px; overflow: hidden;
    background: var(--stage);
    font-family: "Open Sans", Arial, sans-serif;
  }
  .stage {
    position: relative; width: 1200px; height: 1000px;
    display: flex; align-items: center; justify-content: center; gap: 40px;
  }
  .card {
    position: relative; width: 540px; height: 320px;
    background: var(--card); border-radius: 22px; overflow: hidden;
  }
  .card__accent { position: absolute; }
  .card--front .card__accent { left: 250px; top: 0; width: 290px; height: 170px; }
  .card--back .card__accent { left: 200px; top: 0; width: 340px; height: 150px; }

  .contact { position: absolute; left: 40px; top: 120px; }
  .contact__name {
    color: var(--blue); font-weight: 700; font-size: 17px;
    letter-spacing: 0.04em; text-transform: uppercase; margin-bottom: 14px;
  }
  .contact__list { list-style: none; }
  .contact__item {
    display: flex; align-items: flex-start; gap: 10px;
    color: var(--ink); font-size: 13px; line-height: 1.35; margin-bottom: 7px;
  }
  .contact__icon { flex: none; width: 18px; height: 18px; }

  .brand {
    position: absolute; display: flex; align-items: center; gap: 8px;
    color: var(--blue); font-weight: 600; letter-spacing: 0.03em;
  }
  .brand__dot { width: 12px; height: 12px; border-radius: 50%; background: var(--blue); }
  .card--front .brand { right: 36px; bottom: 70px; font-size: 20px; }
  .card--back .brand { right: 40px; bottom: 56px; font-size: 24px; }
</style>
</head>
<body>
<main class="stage">

  <section class="card card--front" aria-label="Business card front">
    <svg class="card__accent" viewBox="0 0 290 170" role="img" aria-label="Decorative blue and orange corner accent">
      <defs>
        <linearGradient id="accentFront" x1="0" y1="1" x2="1" y2="0">
          <stop offset="0" stop-color="#2a6f9e"/>
          <stop offset="1" stop-color="#2f9fd8"/>
        </linearGradient>
      </defs>
      <rect width="290" height="170" fill="url(#accentFront)"/>
      <rect y="150" width="290" height="20" fill="#f0802f"/>
    </svg>

    <div class="contact">
      <p class="contact__name">Dennis Marlow</p>
      <ul class="contact__list">
        <li class="contact__item">
          <svg class="contact__icon" viewBox="0 0 18 18" aria-hidden="true">
            <circle cx="9" cy="9" r="9" fill="var(--orange)"/>
            <path d="M6 5c.6-.4 1.1-.3 1.4.2l.8 1.4c.2.4.1.8-.2 1l-.6.4c.4 1 1.2 1.8 2.2 2.2l.4-.6c.2-.3.6-.4 1-.2l1.4.8c.5.3.6.8.2 1.4-.6.9-1.6 1.1-2.7.6-2-.9-3.5-2.4-4.4-4.4C4.9 6.6 5.1 5.6 6 5z" fill="#fff"/>
          </svg>
          <span>+61 427581962</span>
        </li>
        <li class="contact__item">
          <svg class="contact__icon" viewBox="0 0 18 18" aria-hidden="true">
            <circle cx="9" cy="9" r="9" fill="var(--orange)"/>
            <rect x="4.5" y="6" width="9" height="6.5" rx="1" fill="#fff"/>
            <path d="M4.8 6.4 9 9.6l4.2-3.2" fill="none" stroke="var(--orange)" stroke-width="1"/>
          </svg>
          <span>dennis@qovo.com.au</span>
        </li>
        <li class="contact__item">
          <svg class="contact__icon" viewBox="0 0 18 18" aria-hidden="true">
            <circle cx="9" cy="9" r="9" fill="var(--orange)"/>
            <path d="M9 4a3.2 3.2 0 0 0-3.2 3.2C5.8 9.6 9 13.5 9 13.5s3.2-3.9 3.2-6.3A3.2 3.2 0 0 0 9 4z" fill="#fff"/>
            <circle cx="9" cy="7.2" r="1.2" fill="var(--orange)"/>
          </svg>
          <span>P.O. Box 872 Kelvindale<br>QLD 4309</span>
        </li>
      </ul>
    </div>

    <div class="brand"><span class="brand__dot"></span><span class="brand__name">Qovo International</span></div>
  </section>

  <section class="card card--back" aria-label="Business card back">
    <svg class="card__accent" viewBox="0 0 340 150" role="img" aria-label="Decorative blue and orange corner accent">
      <defs>
        <linearGradient id="accentBack" x1="0" y1="1" x2="1" y2="0">
          <stop offset="0" stop-color="#2a6f9e"/>
          <stop offset="1" stop-color="#2f9fd8"/>
        </linearGradient>
      </defs>
      <rect width="340" height="150" fill="url(#accentBack)"/>
      <rect y="130" width="340" height="20" fill="#f0802f"/>
    </svg>

    <div class="brand"><span class="brand__dot"></span><span class="brand__name">Qovo International</span></div>
  </section>

</main>
</body>
</html>
```